Nail salon window signage design

We need new signage to be designed for our existing nail salon. The sign will be a large sticker that will stick onto the glass window at the front.

Some of the services we provide are:
Manicures
Pedicures
Velora Gel Builder
Acrylic Nails
KVT
Brenlux
Gel Polish
You may wish to have our services listed on the sign but is not compulsory.

I have also attached our logo which can be used on the sign but is not compulsory.

I have also attached a photo of the front of our salon and the sign will be where I have outlined in yellow.

The size of the sign will be 119cm wide and 170cm high.

I am open to any nice classy design you can think of.

```html
<!DOCTYPE html>
<html lang="en">
<head>
<meta charset="utf-8">
<title>Aurelle Nails – Window Sign</title>
<link rel="stylesheet" href="https://fonts.googleapis.com/css2?family=Great+Vibes&family=Poppins:wght@500;700&display=swap">
<style>
  :root {
    --paper: #ffffff;
    --olive: #83734a;
    --olive-light: #b9ad92;
    --burgundy: #8c2036;
    --service-text: #4a3d20;
    --sand: #ecd8b6;
    --sand-deep: #e2c89b;
    --tan: #cfae7a;
    --tan-pale: #efe4d2;
    --skin: #efc2ac;
    --skin-soft: #f6dccf;
  }
  * { margin: 0; padding: 0; box-sizing: border-box; }
  html, body { width: 848px; height: 1200px; overflow: hidden; background: var(--paper); }
  .sign {
    position: relative;
    width: 848px; height: 1200px;
    background: var(--paper);
    overflow: hidden;
    font-family: "Poppins", sans-serif;
  }
  .hero-photo {
    position: absolute; left: 490px; top: 0; width: 358px; height: 370px;
    background: linear-gradient(90deg, rgba(246,220,207,0) 0%, var(--skin-soft) 35%, var(--skin) 100%);
  }
  .brand {
    position: absolute; left: 0; top: 110px; width: 760px;
    text-align: center;
    font-family: "Great Vibes", cursive;
    font-weight: 400;
    font-size: 84px; line-height: 1;
    color: var(--burgundy);
  }
  .tagline {
    position: absolute; left: 0; top: 228px; width: 760px;
    text-align: center;
    font-family: "Great Vibes", cursive;
    font-size: 40px; line-height: 56px;
    color: var(--burgundy);
  }
  .services-band {
    position: absolute; left: 0; top: 369px; width: 848px; height: 68px;
    background: var(--olive);
  }
  .services-title {
    position: absolute; right: 36px; top: 0; height: 68px;
    display: flex; align-items: center;
    color: #fff; font-weight: 700; font-size: 35px; letter-spacing: 0.2px;
  }
  .services-title .star { font-size: 26px; margin: 0 12px; }
  .service-list { position: absolute; left: 388px; top: 470px; width: 460px; list-style: none; }
  .service {
    height: 52px; margin-bottom: 12.5px;
    display: flex; align-items: center; justify-content: flex-end;
    padding-right: 38px;
    background: linear-gradient(90deg, rgba(236,216,182,0) 0%, rgba(236,216,182,0.45) 50%, var(--sand) 96%, var(--sand-deep) 96%);
    color: var(--service-text); font-weight: 500; font-size: 31px; letter-spacing: 0.3px;
  }
  .service .mark { color: var(--burgundy); font-size: 30px; margin-left: 20px; line-height: 1; }
  .feature-photo { position: absolute; left: 0; top: 490px; }
  .polish-photo {
    position: absolute; left: 0; top: 895px; width: 240px; height: 155px;
    background: radial-gradient(ellipse at 40% 50%, #a7a2c2 0%, #e8d98a 45%, rgba(255,255,255,0) 75%);
  }
  .hands-photo {
    position: absolute; left: 380px; top: 915px; width: 468px; height: 285px;
    background: radial-gradient(ellipse at 70% 55%, var(--skin) 0%, var(--skin-soft) 45%, rgba(246,220,207,0) 80%);
  }
  .footer-wave { position: absolute; left: 0; top: 1070px; }
  .website {
    position: absolute; left: 18px; top: 1151px;
    display: flex; align-items: center; gap: 8px;
    color: #fff; font-weight: 500; font-size: 20px;
  }
</style>
</head>
<body>
<main class="sign">
  <div class="hero-photo" role="img" aria-label="Close-up of a woman's chin and hand with metallic gold manicure"></div>

  <h1 class="brand">Aurelle Nails</h1>
  <p class="tagline">Life is not always perfect<br>However your nails should be</p>

  <div class="services-band">
    <h2 class="services-title"><span class="star">★</span>OUR SERVICES<span class="star">★</span></h2>
  </div>

  <svg class="feature-photo" width="380" height="370" viewBox="0 0 380 370">
    <path d="M0 95 C60 20 200 -5 290 50 C370 110 370 260 290 320 C210 375 80 365 0 320 Z" fill="var(--tan-pale)"/>
    <path d="M0 85 C50 15 190 -10 275 45 C350 100 350 250 275 305 C200 360 70 350 0 305 Z" fill="var(--tan)" role="img" aria-label="Hands with colourful abstract nail art"/>
  </svg>

  <ul class="service-list">
    <li class="service">MANICURES<span class="mark">★</span></li>
    <li class="service">PEDICURES<span class="mark">★</span></li>
    <li class="service">VELORA GEL BUILDER<span class="mark">★</span></li>
    <li class="service">ACRYLIC NAILS<span class="mark">★</span></li>
    <li class="service">KVT<span class="mark">★</span></li>
    <li class="service">BRENLUX<span class="mark">★</span></li>
    <li class="service">GEL POLISH<span class="mark">★</span></li>
  </ul>

  <div class="polish-photo" role="img" aria-label="Spilled lilac and yellow nail polish bottles"></div>
  <div class="hands-photo" role="img" aria-label="Hands with natural nude manicure resting on soft fur"></div>

  <svg class="footer-wave" width="848" height="130" viewBox="0 0 848 130">
    <path d="M0 22 C120 -8 260 -2 330 40 C370 65 390 110 420 130 L0 130 Z" fill="var(--olive-light)"/>
    <path d="M0 32 C120 5 250 10 318 50 C360 75 375 112 405 130 L0 130 Z" fill="var(--olive)"/>
  </svg>

  <p class="website">
    <svg width="22" height="22" viewBox="0 0 24 24" fill="none" stroke="#fff" stroke-width="2" aria-hidden="true">
      <circle cx="12" cy="12" r="10"/><path d="M2 12h20M12 2c3 3 3 17 0 20M12 2c-3 3-3 17 0 20"/>
    </svg>
    aurellenails.com.au
  </p>
</main>
</body>
</html>
```